Website to help people naturally reverse diabetes

Wordpress designed with elementor. it is less than 5 pages.
we help people naturally reverse their disease diabetes.
this is my domain www.brightvalewellness.care

(my original website was www.kelmorecenter.care
but we are creating different website for different disease condition starting with diabetes.)

1. home page and with a scheduling option
2. blog page
3. Coach page
4. Contact us

Target Market(s)

1.mid age to older people mostly that are diabetic and it is mostly the American citizens but will be used internationally

Industry/Entity Type

Health care

Coding

Coded - Design and coding required

Number of Pages Required

4 page

Colors
0054AA
0677BA
7BADD7
CADEEF
E8F1F8
00AB8E
00BBA5
67D7C9
C6EFE9
E9F9F6
A7469A
B969AE
D3A5CF
EDDBEB
F8F0F9
6B429C
8869AF
B7A5CE
E3DAEB
F3F0F8

Requirements
Must have
• clean and good fee.l story brand concept a. make the customer the hero. the header page picture should reveal what the customer will feel after the program. Treating the symptom I attached a picture in the file a screen shot.. Normally people treat the symptoms and not the cause. that is 1. closing the tap. 2. remove the block. 3 and them clean he spill over. but do not want to have the picture of medical doctor or nurse. I do not want to offend them we can use the same picture but without them but some way we want to communicate the message.
Nice to have
• more visual feel

```html
<!DOCTYPE html>
<html lang="en">
<head>
<meta charset="utf-8">
<title>Brightvale Wellness – Reverse Diabetes Naturally</title>
<link rel="stylesheet" href="https://fonts.googleapis.com/css2?family=Montserrat:wght@400;500;600;700&display=swap">
<style>
:root{
  --green:#6bbd3c;
  --navy:#3d4876;
  --slate:#8891b5;
  --purple:#5a4b9b;
  --ink:#1d1d22;
  --ring:#e2e3ea;
  --dark:#1d2b2d;
  --white:#ffffff;
}
*{box-sizing:border-box;margin:0;padding:0}
html,body{width:1200px;height:4264px;overflow:hidden;background:var(--white)}
body{position:relative;font-family:'Montserrat',sans-serif;color:var(--ink)}
.abs{position:absolute}

.hero{left:0;top:0;width:1200px;height:720px;
  background:
    radial-gradient(ellipse 260px 140px at 400px 235px,rgba(255,236,200,.95),rgba(255,226,180,0) 70%),
    radial-gradient(ellipse 700px 260px at 420px 260px,rgba(236,214,186,.8),rgba(236,214,186,0) 70%),
    linear-gradient(180deg,rgba(90,82,72,0) 0 58%,rgba(96,86,70,.55) 72%,rgba(70,62,48,.85) 88%,#4d4536 100%),
    radial-gradient(ellipse 180px 260px at 600px 520px,rgba(110,106,102,.55),rgba(110,106,102,0) 80%),
    linear-gradient(180deg,#a99d93 0%,#cdbfb1 22%,#d8cbbd 40%,#c2b6aa 58%,#a99c8c 75%,#8a7d6a 100%)}
.nav{left:261px;top:61px;width:720px;height:36px;background:var(--green);border-radius:18px;color:var(--white);font-weight:600;font-size:18px;letter-spacing:1px}
.nav span{position:absolute;top:8px}
.brand-badge{left:540px;top:44px;width:120px;height:56px;background:var(--white);border-radius:6px;display:flex;align-items:center;justify-content:center;font-weight:700;font-size:15px;color:var(--navy);text-align:center;line-height:1.1}
.wedge{left:0;width:1200px}
.seal{width:112px;height:112px;border-radius:50%;background:#e6e6ea;border:4px solid var(--white);display:flex;align-items:center;justify-content:center;text-align:center;font-weight:700;font-size:14px;color:var(--navy);line-height:1.15}

.feature{width:300px;text-align:center;top:785px}
.feature svg{display:block;margin:0 auto}
.feature h3{margin-top:14px;font-size:26px;font-weight:700;color:var(--green);letter-spacing:1.5px}

.promo{left:88px;top:1130px;width:657px;height:401px;background:var(--slate)}
.promo p{position:absolute;left:72px;top:84px;width:560px;color:var(--white);font-weight:600;font-size:27.5px;line-height:38px;letter-spacing:.6px;text-transform:uppercase}
.btn{position:absolute;left:74px;top:270px;width:320px;height:53px;background:var(--navy);color:var(--white);border-radius:6px;font-weight:600;font-size:18px;letter-spacing:.8px;display:flex;align-items:center;justify-content:center}
.photo-woman{left:745px;top:1031px;width:400px;height:599px;
  background:
    radial-gradient(ellipse 110px 130px at 200px 150px,rgba(214,160,130,.9),rgba(214,160,130,0) 80%),
    radial-gradient(ellipse 170px 140px at 200px 330px,rgba(232,200,205,.95),rgba(232,200,205,0) 85%),
    radial-gradient(ellipse 150px 110px at 170px 500px,rgba(176,112,64,.95),rgba(176,112,64,0) 85%),
    linear-gradient(160deg,#6d7a45 0%,#4d5a33 30%,#6b6150 60%,#3e3426 100%)}

.section-title{left:0;width:1200px;text-align:center;font-weight:600;font-size:44px;letter-spacing:3px;color:var(--ink)}
.method{width:150px;text-align:center;font-size:15.5px;color:var(--purple);line-height:1.15}
.method svg{display:block;margin:0 auto 12px}

.blogs-label{left:0;top:2430px;width:1200px;text-align:center}
.blogs-label span{background:var(--white);padding:0 14px;font-weight:600;font-size:28px;letter-spacing:2px}
.rule{height:1px;background:#c9c9cf}
.blog-main{left:70px;top:2487px;width:759px;height:520px;
  background:
    radial-gradient(ellipse 120px 80px at 600px 230px,rgba(240,170,180,.8),rgba(240,170,180,0) 80%),
    radial-gradient(ellipse 60px 60px at 385px 115px,rgba(248,240,170,.9),rgba(248,240,170,0) 85%),
    linear-gradient(160deg,#46bde0,#22a3d0)}
.blog-bar{left:70px;top:2813px;width:759px;height:194px;background:var(--dark)}
.blog-date{color:var(--white);font-weight:500}
.blog-title{color:var(--green);font-weight:600}
.blog-side{left:882px;width:247px;height:235px}
.side-bar{position:absolute;left:0;bottom:0;width:247px;height:98px;background:rgba(29,43,45,.9);padding:12px 12px}
.side-bar .blog-date{font-size:13px}
.side-bar .blog-title{font-size:15px;line-height:1.2;margin-top:4px;width:200px}
.side-bar small{position:absolute;right:14px;bottom:8px;color:var(--white);font-size:8px}

.coach{width:330px;text-align:center}
.coach .avatar{width:176px;height:176px;border-radius:50%;margin:28px auto 0;background:
  radial-gradient(ellipse 40px 50px at 88px 70px,rgba(226,190,170,.9),rgba(226,190,170,0) 90%),
  linear-gradient(180deg,#6e93ab 0%,#8fb0c4 45%,#eef2f5 70%,#d6dde3 100%)}
.coach h4{margin-top:62px;font-weight:700;font-size:29px;color:var(--navy);letter-spacing:.5px}
.coach p{font-size:21px;color:var(--navy);letter-spacing:1px;margin-top:-4px}

.schedule{left:0;top:3533px;width:1200px;height:252px;background:linear-gradient(90deg,#3c4858,#5b6674 50%,#3f4a5a)}
.schedule h2{position:absolute;top:22px;width:1200px;text-align:center;color:var(--white);font-weight:600;font-size:40px;letter-spacing:2px}
.f-label{position:absolute;height:47px;width:111px;background:var(--navy);color:var(--white);font-weight:700;font-size:25px;letter-spacing:1.5px;display:flex;align-items:center;justify-content:center}
.f-input{position:absolute;height:47px;width:313px;background:var(--white)}
.book{position:absolute;left:1043px;top:91px;width:124px;height:123px;background:var(--navy);color:var(--white);font-weight:600;font-size:27px;line-height:1.15;letter-spacing:2px;display:flex;align-items:center;justify-content:center;text-align:center}

.footer{left:0;top:3785px;width:1200px;height:479px;background:
  radial-gradient(circle 90px at 300px 190px,rgba(255,214,60,.6),rgba(255,214,60,0)),
  radial-gradient(circle 110px at 800px 160px,rgba(255,205,40,.6),rgba(255,205,40,0)),
  radial-gradient(circle 120px at 1000px 330px,rgba(240,180,30,.5),rgba(240,180,30,0)),
  linear-gradient(180deg,#ffffff 0 80px,#7a6220 80px,#d9a21f 48%,#a77816 72%,#3f300f 100%)}
.sub-input{left:70px;top:4008px;width:779px;height:50px;background:var(--white);color:#b4b4ba;font-size:25px;letter-spacing:2px;padding:10px 26px}
.sub-btn{left:849px;top:4008px;width:286px;height:50px;background:var(--navy);color:var(--white);font-weight:600;font-size:25px;letter-spacing:1.5px;display:flex;align-items:center;justify-content:center}
.partner{top:4118px;width:260px;text-align:center;font-weight:700;font-size:38px;color:var(--white)}
.foot-nav{top:4226px;color:var(--white);font-weight:600;font-size:20px;letter-spacing:1px}
</style>
</head>
<body>

<!-- Hero -->
<div class="abs hero" role="img" aria-label="Photo of a woman with arms raised facing a misty sunrise over hills and tall grass"></div>
<nav class="abs nav">
  <span style="left:58px">HOME</span>
  <span style="left:168px">BLOG</span>
  <span style="left:447px">COACH</span>
  <span style="left:569px">CONTACT</span>
</nav>
<div class="abs brand-badge">Kelmore<br>Center</div>

<svg class="abs wedge" style="top:620px" width="1200" height="110" viewBox="0 0 1200 110">
  <polygon points="0,10 600,55 600,60 0,100" fill="var(--green)"/>
  <polygon points="1200,0 620,55 620,60 1200,98" fill="var(--navy)"/>
  <polygon points="0,100 600,60 1200,98 1200,110 0,110" fill="var(--white)"/>
</svg>
<div class="abs seal" style="left:563px;top:626px">Kelmore<br>Center</div>

<!-- Features -->
<div class="abs feature" style="left:93px">
  <svg width="130" height="130" viewBox="0 0 130 130" fill="none" stroke="var(--navy)" stroke-width="4" stroke-linecap="round">
    <circle cx="65" cy="38" r="10"/>
    <path d="M40 50 L58 60 L58 90 L50 115 M90 50 L72 60 L72 90 L80 115 M58 90 L72 90"/>
    <path d="M20 20 v16 M12 28 h16 M110 20 v16 M102 28 h16 M20 100 v16 M12 108 h16 M110 100 v16 M102 108 h16"/>
  </svg>
  <h3>HAPPY LIFE</h3>
</div>
<div class="abs feature" style="left:462px">
  <svg width="130" height="130" viewBox="0 0 130 130" fill="none" stroke="var(--navy)" stroke-width="4">
    <circle cx="65" cy="65" r="58"/>
    <rect x="52" y="34" width="26" height="24"/><rect x="38" y="62" width="26" height="24"/><rect x="66" y="62" width="26" height="24"/>
    <line x1="24" y1="24" x2="106" y2="106"/>
  </svg>
  <h3>NO DIABETICS</h3>
</div>
<div class="abs feature" style="left:798px">
  <svg width="130" height="130" viewBox="0 0 130 130" fill="none" stroke="var(--navy)" stroke-width="4" stroke-linejoin="round">
    <path d="M65 8 L112 22 L112 70 Q112 105 65 124 Q18 105 18 70 L18 22 Z"/>
    <path d="M58 28 h14 v10 h10 v14 h-10 v10 h-14 v-10 h-10 v-14 h10 Z"/>
    <circle cx="42" cy="76" r="7"/><circle cx="88" cy="76" r="7"/><circle cx="65" cy="86" r="6"/>
  </svg>
  <h3>HEALTHY LIFE</h3>
</div>

<!-- Promo -->
<div class="abs promo">
  <p>You shouldn't have to be on medication for the rest of your life. It's expensive and can cause side effects…</p>
  <div class="btn">BOOK AN APPOINTMENT</div>
</div>
<div class="abs photo-woman" role="img" aria-label="Photo of a smiling woman on a park bench holding a basket of bread and grapes"></div>

<!-- Methods -->
<h2 class="abs section-title" style="top:1685px">OUR METHODS</h2>
<svg class="abs" style="left:288px;top:1769px" width="600" height="600" viewBox="-300 -300 600 600">
  <circle r="295" fill="none" stroke="var(--ring)" stroke-width="5"/>
  <circle r="146" fill="none" stroke="var(--ring)" stroke-width="5"/>
  <g stroke="var(--white)" stroke-width="10">
    <line x1="0" y1="-140" x2="0" y2="-300"/>
    <line x1="0" y1="-140" x2="0" y2="-300" transform="rotate(45)"/>
    <line x1="0" y1="-140" x2="0" y2="-300" transform="rotate(90)"/>
    <line x1="0" y1="-140" x2="0" y2="-300" transform="rotate(135)"/>
    <line x1="0" y1="-140" x2="0" y2="-300" transform="rotate(180)"/>
    <line x1="0" y1="-140" x2="0" y2="-300" transform="rotate(225)"/>
    <line x1="0" y1="-140" x2="0" y2="-300" transform="rotate(270)"/>
    <line x1="0" y1="-140" x2="0" y2="-300" transform="rotate(315)"/>
  </g>
  <g stroke="var(--ring)" stroke-width="4">
    <line x1="0" y1="-148" x2="0" y2="-293" transform="rotate(4)"/>
    <line x1="0" y1="-148" x2="0" y2="-293" transform="rotate(49)"/>
    <line x1="0" y1="-148" x2="0" y2="-293" transform="rotate(94)"/>
    <line x1="0" y1="-148" x2="0" y2="-293" transform="rotate(139)"/>
    <line x1="0" y1="-148" x2="0" y2="-293" transform="rotate(184)"/>
    <line x1="0" y1="-148" x2="0" y2="-293" transform="rotate(229)"/>
    <line x1="0" y1="-148" x2="0" y2="-293" transform="rotate(274)"/>
    <line x1="0" y1="-148" x2="0" y2="-293" transform="rotate(319)"/>
  </g>
  <g fill="var(--ring)">
    <polygon points="-8,-200 -8,-250 -40,-225"/>
    <polygon points="-8,-200 -8,-250 -40,-225" transform="rotate(45)"/>
    <polygon points="-8,-200 -8,-250 -40,-225" transform="rotate(90)"/>
    <polygon points="-8,-200 -8,-250 -40,-225" transform="rotate(135)"/>
    <polygon points="-8,-200 -8,-250 -40,-225" transform="rotate(180)"/>
    <polygon points="-8,-200 -8,-250 -40,-225" transform="rotate(225)"/>
    <polygon points="-8,-200 -8,-250 -40,-225" transform="rotate(270)"/>
    <polygon points="-8,-200 -8,-250 -40,-225" transform="rotate(315)"/>
  </g>
</svg>

<div class="abs method" style="left:433px;top:1813px">
  <svg width="40" height="40" viewBox="0 0 40 40" fill="none" stroke="var(--purple)" stroke-width="2.5" stroke-linecap="round"><circle cx="12" cy="8" r="5"/><circle cx="28" cy="8" r="5"/><path d="M4 36 v-14 q8 -6 16 0 q8 -6 16 0 v14"/></svg>
  Counselling/<br>Stress<br>Management
</div>
<div class="abs method" style="left:592px;top:1813px">
  <svg width="40" height="40" viewBox="0 0 40 40" fill="none" stroke="var(--purple)" stroke-width="2.5" stroke-linejoin="round"><rect x="6" y="14" width="28" height="22" rx="2"/><path d="M12 14 v-8 h16 v8 M14 24 h12"/></svg>
  Healthy<br>Grocery Shopping
</div>
<div class="abs method" style="left:723px;top:1955px">
  <svg width="40" height="40" viewBox="0 0 40 40" fill="none" stroke="var(--purple)" stroke-width="2.5" stroke-linecap="round"><path d="M4 22 h32 q-2 12 -16 12 q-14 0 -16 -12"/><circle cx="16" cy="14" r="4"/><circle cx="27" cy="10" r="4"/></svg>
  Hydrotherapy
</div>
<div class="abs method" style="left:715px;top:2118px">
  <svg width="40" height="40" viewBox="0 0 40 40" fill="none" stroke="var(--purple)" stroke-width="2.5" stroke-linecap="round"><path d="M2 20 h36 M7 10 v20 M33 10 v20 M12 13 v14 M28 13 v14"/></svg>
  Fitness Program
</div>
<div class="abs method" style="left:604px;top:2237px">
  <svg width="40" height="40" viewBox="0 0 40 40" fill="none" stroke="var(--purple)" stroke-width="2.5" stroke-linejoin="round"><path d="M14 4 h12 M16 4 v12 l-9 18 h26 l-9 -18 v-12"/><path d="M11 26 h18"/></svg>
  Health Education
</div>
<div class="abs method" style="left:425px;top:2222px">
  <svg width="40" height="40" viewBox="0 0 40 40" fill="none" stroke="var(--purple)" stroke-width="2.5" stroke-linecap="round"><circle cx="20" cy="8" r="5"/><path d="M4 30 h32 M8 30 v6 M32 30 v6 M10 30 l6 -14 h8 l6 14"/></svg>
  Therapeutic<br>Massage
</div>
<div class="abs method" style="left:306px;top:2109px">
  <svg width="40" height="40" viewBox="0 0 40 40" fill="none" stroke="var(--purple)" stroke-width="2.5" stroke-linecap="round"><path d="M4 20 q2 14 16 14 q14 0 16 -14 Z M26 16 l10 -10"/><circle cx="12" cy="10" r="2"/><circle cx="20" cy="6" r="2"/></svg>
  Cooking
</div>
<div class="abs method" style="left:304px;top:1944px">
  <svg width="40" height="40" viewBox="0 0 40 40" fill="none" stroke="var(--purple)" stroke-width="2.5" stroke-linecap="round"><path d="M20 12 q-14 -6 -14 10 q0 14 14 14 q14 0 14 -14 q0 -16 -14 -10 Z M20 12 l4 -8"/></svg>
  Nutrition<br>Empowerment
</div>

<!-- Blogs -->
<div class="abs rule" style="left:130px;top:2449px;width:960px"></div>
<div class="abs blogs-label"><span>MY BLOGS</span></div>

<div class="abs blog-main" role="img" aria-label="Photo of a syringe, pills and sticky notes on a blue background"></div>
<div class="abs blog-bar">
  <div class="abs blog-date" style="left:62px;top:26px;font-size:29px">September 14,2020</div>
  <div class="abs blog-title" style="left:62px;top:66px;width:520px;font-size:36px;line-height:43px;letter-spacing:1px">Why Diabetics is more Dangerous ?</div>
  <div class="abs rule" style="left:62px;top:160px;width:300px;background:#7c8a8c"></div>
  <div class="abs" style="left:407px;top:154px;color:var(--white);font-size:14px;font-weight:500">by Dr. Mara Ellison</div>
  <svg class="abs" style="left:672px;top:36px" width="46" height="56" viewBox="0 0 46 56"><path d="M3 3 h40 v50 l-20 -16 l-20 16 Z" fill="none" stroke="var(--white)" stroke-width="4"/></svg>
</div>

<div class="abs blog-side" style="top:2487px;background:radial-gradient(ellipse 70px 90px at 190px 60px,rgba(214,150,130,.9),rgba(214,150,130,0) 90%),linear-gradient(180deg,#f6a9c4,#f2b8c6 60%,#d9a08d)" role="img" aria-label="Photo of a person's torso against a pink background">
  <div class="side-bar">
    <div class="blog-date">Feburary 14,2021</div>
    <div class="blog-title">Is Diabetics is Mother of all diseases.</div>
    <small>by Dr. Mara Ellison</small>
    <svg class="abs" style="right:14px;top:12px" width="14" height="18" viewBox="0 0 14 18"><path d="M1 1 h12 v16 l-6 -5 l-6 5 Z" fill="none" stroke="var(--white)" stroke-width="1.5"/></svg>
  </div>
</div>
<div class="abs blog-side" style="top:2772px;background:linear-gradient(180deg,#cfd8e2,#9aa6b4 40%,#6b7582 65%,#4a4234)" role="img" aria-label="Photo of a tall hotel building">
  <div class="side-bar">
    <div class="blog-date">Feburary 14,2021</div>
    <div class="blog-title">Is Hoteling safe?</div>
    <small>by Dr. Mara Ellison</small>
    <svg class="abs" style="right:14px;top:12px" width="14" height="18" viewBox="0 0 14 18"><path d="M1 1 h12 v16 l-6 -5 l-6 5 Z" fill="none" stroke="var(--white)" stroke-width="1.5"/></svg>
  </div>
</div>

<!-- Coaches -->
<h2 class="abs section-title" style="top:3057px">OUR COACHES</h2>
<svg class="abs" style="left:0;top:3165px" width="1200" height="240" viewBox="0 0 1200 240">
  <g fill="none" stroke="var(--green)" stroke-linecap="round" stroke-dasharray="0 14">
    <circle cx="215" cy="120" r="116" stroke-width="7"/><circle cx="215" cy="120" r="104" stroke-width="5"/>
    <circle cx="589" cy="120" r="116" stroke-width="7"/><circle cx="589" cy="120" r="104" stroke-width="5"/>
    <circle cx="965" cy="120" r="116" stroke-width="7"/><circle cx="965" cy="120" r="104" stroke-width="5"/>
  </g>
</svg>
<div class="abs coach" style="left:50px;top:3169px"><div class="avatar" role="img" aria-label="Portrait photo of a female doctor in a white coat"></div><h4>DR. HOLLIS</h4><p>JUNIOR DOCTOR</p></div>
<div class="abs coach" style="left:424px;top:3169px"><div class="avatar" role="img" aria-label="Portrait photo of a senior male doctor in a white coat"></div><h4>DR. HOLLIS</h4><p>SPECIALIST</p></div>
<div class="abs coach" style="left:800px;top:3169px"><div class="avatar" role="img" aria-label="Portrait photo of a female doctor in a white coat"></div><h4>DR. HOLLIS</h4><p>SENIOR DOCTOR</p></div>

<!-- Schedule -->
<section class="abs schedule" role="img" aria-label="Blurred photo of a clinic room behind the booking form">
  <h2>SCHEDULE THE MEETING</h2>
  <div class="f-label" style="left:61px;top:91px">NAME:</div><div class="f-input" style="left:172px;top:91px"></div>
  <div class="f-label" style="left:559px;top:91px">EMAIL:</div><div class="f-input" style="left:670px;top:91px"></div>
  <div class="f-label" style="left:61px;top:167px">TIME:</div><div class="f-input" style="left:172px;top:167px"></div>
  <div class="f-label" style="left:559px;top:167px">DATE:</div><div class="f-input" style="left:670px;top:167px"></div>
  <div class="book">BOOK<br>NOW</div>
</section>

<!-- Footer -->
<div class="abs footer" role="img" aria-label="Photo of many yellow smiley balls"></div>
<svg class="abs wedge" style="top:3855px" width="1200" height="100" viewBox="0 0 1200 100">
  <polygon points="0,10 560,55 0,80" fill="var(--green)"/>
  <polygon points="1200,2 660,50 1200,90" fill="var(--navy)"/>
</svg>
<div class="abs seal" style="left:553px;top:3891px">Kelmore<br>Center</div>
<div class="abs sub-input">ENTER YOUR EMAIL</div>
<div class="abs sub-btn">SUBSCRIBE NOW</div>
<div class="abs partner" style="left:135px">Norvale</div>
<div class="abs partner" style="left:482px">Ashgrove</div>
<div class="abs partner" style="left:871px">Tesk</div>
<div class="abs rule" style="left:0;top:4212px;width:1200px;background:rgba(255,255,255,.7)"></div>
<div class="abs foot-nav" style="left:97px">HOME</div>
<div class="abs foot-nav" style="left:386px">BLOG</div>
<div class="abs foot-nav" style="left:714px">COACH</div>
<div class="abs foot-nav" style="left:1011px">CONTACT</div>

</body>
</html>
```